IT Company looking to market towards Dental Offices

I am looking for a full-color design. Using my existing logo. Must have High Res stock photos. The brochure needs to be full page edge to edge design single fold pamphlet style. Content provided. Please see the website in attached Word Doc for more content.

```html
<!DOCTYPE html>
<html lang="en">
<head>
<meta charset="utf-8">
<title>Northgate Techs – Managed Services Brochure</title>
<link href="https://fonts.googleapis.com/css2?family=Audiowide&family=Open+Sans:wght@400;600;700&display=swap" rel="stylesheet">
<style>
  :root{
    --navy:#2a2f86;
    --navy-deep:#1f2470;
    --blue:#1e5bc6;
    --bright:#2f74e4;
    --ink:#2b2f5a;
    --muted:#5a5f80;
    --paper:#ffffff;
    --stage:#d9d9de;
    --heading:'Audiowide', sans-serif;
    --body:'Open Sans', sans-serif;
  }
  *{box-sizing:border-box;margin:0;padding:0}
  html,body{width:1200px;height:1200px;overflow:hidden;background:var(--stage);font-family:var(--body);color:var(--ink)}
  .canvas{position:relative;width:1200px;height:1200px}
  .spread{position:absolute;left:160px;width:880px;height:569px;box-shadow:0 10px 30px rgba(0,0,0,.18)}
  .spread--outside{top:20px}
  .spread--inside{top:609px}
  .page{position:absolute;top:0;width:440px;height:569px;background:var(--paper);overflow:hidden}
  .page--left{left:0}
  .page--right{left:440px;border-left:1px solid #e6e7ee}
  .art{position:absolute;inset:0;width:440px;height:569px}
  .photo{position:absolute;border-radius:50%}
  .photo--chips{background:radial-gradient(circle at 45% 45%,#b99a5c 0%,#5f6b45 25%,#27533c 55%,#173429 100%)}
  .photo--vault{background:radial-gradient(circle at 55% 50%,#e4e6ea 0%,#aeb3ba 45%,#6d737c 80%,#8e8578 100%)}
  .photo--board{background:radial-gradient(circle at 40% 40%,#7fc2f0 0%,#2d63b8 50%,#1d2b6e 100%);border:4px solid var(--blue)}
  .photo--drive{background:radial-gradient(circle at 50% 50%,#e7e9ee 0%,#8d96a8 50%,#2c3656 100%);border:4px solid var(--blue)}
  .brand{position:absolute;display:flex;align-items:center;gap:8px;font-family:var(--heading);color:var(--navy);white-space:nowrap}
  .brand__dot{border-radius:50%;border:3px solid var(--blue);flex:none}
  .brand--cover{left:30px;top:36px;font-size:15px}
  .brand--cover .brand__dot{width:28px;height:28px}
  .brand--back{left:250px;top:160px;font-size:12px}
  .brand--back .brand__dot{width:20px;height:20px;border-width:2px}
  .cover-title{position:absolute;left:30px;top:468px;font-family:var(--heading);color:var(--navy);line-height:1.1}
  .cover-title__main{display:block;font-size:26px;letter-spacing:.5px}
  .cover-title__sub{display:block;font-size:21px}
  .cover-url{position:absolute;left:30px;top:528px;font-size:11px;font-weight:600;color:var(--blue);display:flex;align-items:center;gap:5px}
  .cover-url::before{content:"";width:8px;height:8px;border-radius:50%;background:var(--blue)}
  .band-note{position:absolute;color:#fff;font-size:7.5px;line-height:1.4}
  .band-note--cover{right:22px;bottom:10px;width:150px;text-align:right}
  .section-title{font-family:var(--heading);color:var(--navy);font-size:19px;text-transform:uppercase;display:flex;align-items:center;gap:10px;white-space:nowrap}
  .section-title::after{content:"";flex:1;height:2px;background:var(--bright)}
  .section-title--light{color:#fff}
  .vault-copy{position:absolute;left:36px;top:36px;width:370px}
  .vault-copy .section-title{font-size:21px;text-transform:none}
  .vault-copy p{font-size:8.5px;line-height:1.5;color:var(--muted);margin-top:8px}
  .vault-copy a{color:var(--blue);font-weight:700;text-decoration:none}
  .block{position:absolute}
  .list-cols{display:grid;grid-template-columns:1fr 1fr;gap:0 10px;margin-top:7px}
  .list{list-style:none}
  .list li{font-size:9px;line-height:1.6;padding-left:11px;position:relative}
  .list li::before{content:"";position:absolute;left:0;top:5px;width:5px;height:5px;background:var(--blue)}
  .note{font-size:8.5px;line-height:1.5;color:var(--muted)}
  .about{position:absolute;left:30px;top:458px;width:380px;color:#fff}
  .about p{font-size:8px;line-height:1.5;margin-top:6px;opacity:.92}
  .about .tagline{font-size:12px;font-weight:600;opacity:1;margin-top:6px}
  .ready-title{font-family:var(--heading);color:var(--navy);font-size:19px;line-height:1.15;text-transform:uppercase}
  .ready-lead{font-size:9.5px;font-weight:600;margin:7px 0 4px}
  .steps{list-style:none;counter-reset:step}
  .steps li{counter-increment:step;font-size:9px;line-height:1.8;display:flex;align-items:center;gap:6px}
  .steps li::before{content:counter(step);width:13px;height:13px;border-radius:50%;border:1.5px solid var(--blue);color:var(--blue);font-size:7.5px;font-weight:700;display:flex;align-items:center;justify-content:center}
  .band-note--inside{left:30px;right:30px;bottom:40px}
</style>
</head>
<body>
<main class="canvas">

  <!-- Outside: back panel + front cover -->
  <section class="spread spread--outside">
    <article class="page page--left back-panel">
      <svg class="art" viewBox="0 0 440 569" aria-hidden="true">
        <circle cx="150" cy="420" r="200" fill="var(--navy)"/>
        <circle cx="160" cy="420" r="214" fill="none" stroke="var(--bright)" stroke-width="3"/>
      </svg>
      <div class="photo photo--vault" style="left:-50px;top:238px;width:370px;height:370px" role="img" aria-label="Photo of a steel bank vault door"></div>
      <div class="vault-copy">
        <h2 class="section-title">DentaLocker.com</h2>
        <p>Offsite backups for your practice management software made easy and automated. We know how to configure your dental software so every chart and image is protected and ready to restore.</p>
        <p>Get started today at <a>www.dentalocker.com</a>. We don't charge anything until we have confirmation that your data has been successfully backed up to our encrypted servers.</p>
      </div>
      <div class="brand brand--back"><span class="brand__dot"></span>Northgate Techs</div>
    </article>

    <article class="page page--right cover">
      <svg class="art" viewBox="0 0 440 569" aria-hidden="true">
        <circle cx="315" cy="262" r="175" fill="var(--navy)"/>
        <circle cx="305" cy="265" r="188" fill="none" stroke="var(--bright)" stroke-width="3"/>
        <path d="M0 560 Q220 540 440 505 L440 569 L0 569 Z" fill="var(--navy)"/>
      </svg>
      <div class="photo photo--chips" style="left:170px;top:90px;width:330px;height:330px" role="img" aria-label="Close-up photo of processors and memory circuit boards"></div>
      <div class="brand brand--cover"><span class="brand__dot"></span>Northgate Techs</div>
      <h1 class="cover-title">
        <span class="cover-title__main">EXTRAORDINARY</span>
        <span class="cover-title__sub">Managed Services</span>
      </h1>
      <div class="cover-url">www.northgatetechs.com</div>
      <p class="band-note band-note--cover">Secure, reliable IT support built for busy dental practices.</p>
    </article>
  </section>

  <!-- Inside spread -->
  <section class="spread spread--inside">
    <article class="page page--left">
      <svg class="art" viewBox="0 0 440 569" aria-hidden="true">
        <path d="M0 430 Q200 470 440 455 L440 569 L0 569 Z" fill="var(--navy)"/>
      </svg>
      <div class="photo photo--board" style="left:30px;top:50px;width:90px;height:90px" role="img" aria-label="Photo of a blue-lit circuit board"></div>
      <div class="photo photo--drive" style="left:92px;top:18px;width:72px;height:72px" role="img" aria-label="Photo of computer components"></div>

      <div class="block" style="left:30px;top:158px;width:300px">
        <h3 class="section-title">Hardware Sales</h3>
        <div class="list-cols">
          <ul class="list"><li>Servers</li><li>Workstations</li><li>Firewalls</li><li>Routers</li></ul>
          <ul class="list"><li>Switches</li><li>TV's &amp; Monitors</li><li>Wireless Equipment</li><li>Custom Check-in Workstations</li></ul>
        </div>
      </div>

      <div class="block" style="left:30px;top:268px;width:330px">
        <h3 class="section-title">Infrastructure</h3>
        <div class="list-cols">
          <ul class="list"><li>Data &amp; Voice Cable</li><li>HDMI &amp; COAX Video Cable</li><li>TV &amp; Dual Monitor Installation</li><li>Mounting Hardware</li></ul>
          <ul class="list"><li>Wireless Installation</li><li>Office Sound Solutions</li><li>Custom Data Cable</li><li>Video Surveillance</li></ul>
        </div>
        <p class="note" style="margin-top:10px">We collaborate everything and everyone for you, make one call to us and let us handle your technology.</p>
      </div>

      <div class="about">
        <h3 class="section-title section-title--light">About Us</h3>
        <p>Northgate Techs offers a proven expertise in Dental Practices. We have trained engineers that specialize in dental imaging, X-ray sensors, intraoral cameras and practice software, so your office keeps running.</p>
        <p class="tagline">We know Dental!</p>
      </div>
    </article>

    <article class="page page--right">
      <svg class="art" viewBox="0 0 440 569" aria-hidden="true">
        <path d="M0 455 Q220 470 440 462 L440 569 L0 569 Z" fill="var(--navy)"/>
      </svg>
      <div class="photo photo--drive" style="left:250px;top:58px;width:70px;height:70px" role="img" aria-label="Photo of an open hard drive"></div>
      <div class="photo photo--board" style="left:312px;top:28px;width:84px;height:84px" role="img" aria-label="Photo of network cabling"></div>

      <div class="block" style="left:30px;top:140px;width:385px">
        <h3 class="section-title">Solutions</h3>
        <div class="list-cols" style="grid-template-columns:1.15fr 1fr">
          <ul class="list"><li>Flat Rate Monthly Support</li><li>Secure Backups with our DentaLocker.com</li><li>Secure Encrypted Emails &amp; X-Rays</li><li>Practice Management Software Experts</li><li>HIPAA Compliance</li></ul>
          <ul class="list"><li>Anti-Virus, Anti-Malware and Cyber Security</li><li>Data Recovery</li><li>Cloud Office &amp; Email Apps</li><li>Phone VOIP &amp; SIP Trunks</li></ul>
        </div>
      </div>

      <div class="block" style="left:30px;top:278px;width:385px">
        <h3 class="ready-title">Ready to make your<br>technology work?</h3>
        <p class="ready-lead">How To Achieve Technology Bliss for Your Practice</p>
        <ol class="steps">
          <li>Schedule a FREE Network &amp; Technology Evaluation</li>
          <li>Receive your Flat Rate Price and Technology Quote</li>
          <li>Sit back and let Northgate Techs take care of everything.</li>
        </ol>
        <p class="note" style="margin-top:8px">Don't let Technology Departments, Hardware Vendors and Practice Management Vendors Point Fingers at each other.</p>
      </div>

      <p class="band-note band-note--inside">We can handle supporting your practice management software, including imaging bridges and sensors, providing the correct configuration the first time.</p>
    </article>
  </section>

</main>
</body>
</html>
```